Business card for Autism Consultancy

I need a double-sided business card for Brightpath Kinder Consultancy
Please try to use the colours and graphics in line with our website www.brightpathkinder.nz
Front side
Logo and the name of the company – Brightpath Kinder Consultancy
We use Child-Centred, Modern and Innovative approaches
Teaching autistic children to bond, laugh and play
www.brightpathkinder.nz
info@brightpathkinder.nz
phone +64 09 37 815 66
Back side
Photo
Orla Fennimore
Founder
Postgraduate Autism (Children) Specialist (with Merit)
Qualified by the Faculty of Learning Support and Wellbeing Studies (FLSW), University of Thornvale
orla@brightpathkinder.nz
phone +64 937 815 66
mobile: +64 20 6283 9145
Please do not convert the text fields to outlines, i.e. I need to be able to edit any text after.
The final design should be either in Adobe Illustrator or Adobe Photoshop format.
The Specs for the business card are:
Full Bleed Size
94 x 58 mm
1110 x 685 pixels
Document Trim Size
91 x 55 mm
1075 x 650 pixels

```html
<!DOCTYPE html>
<html lang="en">
<head>
<meta charset="utf-8">
<title>Brightpath Kinder Consultancy – Business Card</title>
<link rel="stylesheet" href="https://fonts.googleapis.com/css2?family=Arimo:wght@400;700&family=Archivo+Black&display=swap">
<style>
  :root {
    --yellow: #ffd226;
    --teal: #52c5c1;
    --navy: #1f2a5c;
    --ink: #111111;
    --grey: #e3e3e3;
    --white: #ffffff;
    --backdrop: #2b2b2e;
  }
  * { box-sizing: border-box; margin: 0; padding: 0; }
  html, body { width: 1200px; height: 809px; overflow: hidden; }
  body {
    background: var(--backdrop);
    font-family: "Arimo", Arial, sans-serif;
    position: relative;
  }
  .card {
    position: absolute;
    top: 232px;
    width: 570px;
    height: 345px;
    overflow: hidden;
    box-shadow: 0 10px 24px rgba(0,0,0,.45);
  }
  .card--profile { left: 20px; background: var(--yellow); }
  .card--company { left: 610px; background: var(--white); }
  .card svg.shapes { position: absolute; inset: 0; }
  .text { position: absolute; color: var(--ink); }

  /* profile side */
  .portrait {
    position: absolute; left: 40px; top: 60px; width: 180px; height: 180px;
    border-radius: 50%; background: var(--white); padding: 10px;
  }
  .portrait__photo {
    width: 100%; height: 100%; border-radius: 50%;
    background: radial-gradient(circle at 50% 40%, #e2b49a 0%, #b98467 45%, #4a3a32 100%);
  }
  .founder-name {
    left: 250px; top: 52px;
    font-family: "Archivo Black", "Arial Black", sans-serif;
    font-size: 21px; letter-spacing: .3px;
  }
  .founder-credentials {
    left: 250px; top: 96px; width: 300px;
    font-size: 11.5px; line-height: 1.35;
  }
  .founder-email { left: 340px; top: 191px; font-size: 12px; }

  /* company side */
  .company-name {
    left: 70px; top: 58px;
    font-weight: 700; font-size: 30px; line-height: 1.1; color: var(--navy);
  }
  .company-mark {
    position: absolute; left: 30px; top: 66px; width: 28px; height: 28px;
    border-radius: 50%; background: var(--yellow);
  }
  .phones { left: 150px; top: 208px; font-size: 12.5px; line-height: 1.35; }
  .web { left: 380px; top: 180px; font-size: 12px; line-height: 1.35; }
  .tagline {
    left: 30px; top: 262px;
    font-weight: 700; font-size: 13px; line-height: 1.3;
  }
</style>
</head>
<body>

<section class="card card--profile" aria-label="Profile side">
  <svg class="shapes" width="570" height="345" viewBox="0 0 570 345" aria-hidden="true">
    <polygon points="300,176 570,176 570,214 326,214 314,238 290,238" fill="var(--teal)"/>
    <g fill="none" stroke="var(--white)" stroke-width="2">
      <rect x="302" y="193" width="24" height="16" rx="2"/>
      <line x1="308" y1="213" x2="320" y2="213"/>
    </g>
  </svg>
  <div class="portrait"><div class="portrait__photo" role="img" aria-label="Portrait photo of the founder"></div></div>
  <p class="text founder-name">ORLA FENNIMORE (Founder)</p>
  <p class="text founder-credentials">Postgraduate Autism (Children) Specialist (with Merit) Qualified by the Faculty of Learning Support and Wellbeing Studies (FLSW), University of Thornvale</p>
  <p class="text founder-email">orla@brightpathkinder.nz</p>
</section>

<section class="card card--company" aria-label="Company side">
  <svg class="shapes" width="570" height="345" viewBox="0 0 570 345" aria-hidden="true">
    <polygon points="260,0 570,0 570,250 420,160" fill="var(--teal)"/>
    <rect x="0" y="250" width="500" height="42" fill="var(--grey)"/>
    <polygon points="0,214 500,214 500,250 0,250" fill="var(--yellow)"/>
    <polygon points="360,170 540,170 540,214 360,214" fill="var(--yellow)"/>
    <rect x="86" y="196" width="52" height="50" rx="6" fill="var(--teal)"/>
    <g fill="var(--white)">
      <path d="M97 213 q15 -8 30 0 v4 h-7 v-3 q-8 -3 -16 0 v3 h-7z"/>
      <rect x="103" y="220" width="18" height="14" rx="2"/>
    </g>
    <rect x="318" y="164" width="52" height="50" rx="6" fill="var(--teal)"/>
    <g fill="none" stroke="var(--white)" stroke-width="2">
      <rect x="332" y="178" width="24" height="16" rx="2"/>
      <line x1="338" y1="198" x2="350" y2="198"/>
    </g>
  </svg>
  <span class="company-mark" aria-hidden="true"></span>
  <p class="text company-name">Brightpath Kinder<br>Consultancy</p>
  <p class="text phones">+64 09 37 815 66<br>+64 20 6283 9145</p>
  <p class="text web">www.brightpathkinder.nz<br>info@brightpathkinder.nz</p>
  <p class="text tagline">We use Child-Centred, Modern and Innovative approaches<br>Teaching autistic children to bond, laugh and play</p>
</section>

</body>
</html>
```